Text Marketing Tri-Fold Brochure

I am looking for a modern, full page brochure (tri-fold desgin) to email or mail to restaurant owners or ownership groups. The brochure should advertise our subscription-based text marketing service. Information on our service can be found at http://www.qelvaro.com/mobile-marketing/. Please do not just copy the elements on the site. The brochure should be be clean, crisp, and visually appealing as it might be the first impression a prospect will see from the company.

The final design should communicate increased sales through utilization of mobile coupons.
Updates

Target Market(s)

Restaurant owners, more often male, age 30-65

Industry/Entity Type

Restaurant

Requirements
Must have
• Flyer should be front and back with a tri-fold design.

Use of the official Qelvaro logo. Logo should have a registered mark at the end of the word Qelvaro.
Nice to have
• Utilization of "Marketing @ the Pace of TradeMind" with a registered mark on TradeMind OR "Powering Restaurants to Mobile Success"

```html
<!DOCTYPE html>
<html lang="en">
<head>
<meta charset="utf-8">
<title>Qelvaro Mobile Marketing Tri-Fold</title>
<link rel="stylesheet" href="https://fonts.googleapis.com/css2?family=Questrial&family=Tinos&display=swap">
<style>
  :root{
    --page:#e9e9ea;
    --brick:#9a3733;
    --brick-dark:#7f2b28;
    --ink:#2b2b2b;
    --icon:#474a4f;
    --blue:#2e95d6;
    --card:#ffffff;
    --white:#ffffff;
  }
  *{margin:0;padding:0;box-sizing:border-box}
  html,body{width:1200px;height:473px;overflow:hidden;background:var(--page)}
  body{position:relative;font-family:"Questrial",sans-serif;color:var(--ink)}

  /* Outside panel */
  .cover{position:absolute;left:13px;top:13px;width:580px;height:447px;overflow:hidden;
    background:linear-gradient(180deg,#ffffff 0%,#f3f3f3 55%,#bdbec0 100%)}
  .steps{position:absolute;left:18px;top:0;width:157px;height:447px;background:var(--brick);
    color:var(--white);text-align:center;padding-top:34px;font-size:11px;line-height:13px}
  .steps p{margin-bottom:9px}
  .sweep{position:absolute;left:193px;top:0;width:387px;height:175px}
  .art{position:absolute;left:399px;top:78px;width:150px;height:176px;border-radius:8px;
    background:radial-gradient(circle at 50% 45%,#9cc3df 0%,#5f6b78 55%,rgba(60,60,60,0) 75%)}
  .contact{position:absolute;left:193px;top:311px;width:193px;height:136px;background:var(--brick);
    color:var(--white);font-family:Arial,sans-serif;font-size:7.3px;line-height:9px;text-align:center;
    padding-top:54px}
  .brand{position:absolute;left:402px;top:327px;width:161px;height:104px;border-radius:10px;
    background:var(--white);display:flex;align-items:center;justify-content:center;gap:7px}
  .brand-mark{width:16px;height:16px;background:var(--brick)}
  .brand-name{font-size:20px;letter-spacing:1px;color:#3a3a3a}
  .brand-name sup{font-size:8px}

  /* Inside panel */
  .features{position:absolute;left:608px;top:13px;width:580px;height:447px;overflow:hidden;
    background:radial-gradient(ellipse at 50% 40%,#f4f4f4 0%,#b9b9b9 50%,#6c6c6c 100%)}
  .card{position:absolute;width:175px;height:110px;background:var(--card);border-radius:6px;
    box-shadow:0 1px 3px rgba(0,0,0,.35)}
  .card-title{position:absolute;left:14px;right:-6px;top:0;height:19px;background:var(--blue);
    border-radius:4px 0 0 0;color:var(--white);font-family:"Tinos",serif;font-size:9px;
    line-height:19px;text-align:center}
  .card-icon{position:absolute;left:9px;top:32px;width:48px;height:48px}
  .card-text{position:absolute;left:64px;top:25px;width:104px;font-size:5.9px;line-height:6.6px;color:#333}
  .c1{left:19px}.c2{left:212px}.c3{left:404px}
  .r1{top:17px}.r2{top:147px}.r3{top:282px}
  .tagline{position:absolute;left:0;bottom:0;width:580px;height:42px;background:var(--brick);
    color:var(--white);font-family:"Tinos",serif;font-size:10px;line-height:12px;text-align:center;padding-top:9px}
  .tagline sup{font-size:6px}
</style>
</head>
<body>

<section class="cover">
  <div class="steps">
    <p>Customers Subscribe<br>to Your Service</p>
    <p>You Schedule a<br>Mobile Campaign</p>
    <p>Customers Receive<br>Mobile Coupons</p>
    <p>Customers Redeem<br>Mobile Coupons</p>
  </div>
  <svg class="sweep" viewBox="0 0 387 175" aria-hidden="true">
    <defs>
      <linearGradient id="sweepFill" x1="0" y1="0" x2="1" y2="0">
        <stop offset="0" stop-color="#1c1c1c"/>
        <stop offset="1" stop-color="#9a3733"/>
      </linearGradient>
    </defs>
    <path d="M0 0H387V52Q170 62 0 175Z" fill="url(#sweepFill)"/>
  </svg>
  <div class="art" role="img" aria-label="Illustration of a cartoon bird carrying an envelope above a smartphone"></div>
  <div class="contact">
    418 Harlow Ave.<br>
    Brindale, FL 32190<br>
    Toll Free (888) 555-0172<br>
    sales@qelvaro.com | support@qelvaro.com
  </div>
  <div class="brand">
    <span class="brand-mark"></span>
    <span class="brand-name">QELVARO<sup>®</sup></span>
  </div>
</section>

<section class="features">
  <article class="card c1 r1">
    <h3 class="card-title">Redemption System</h3>
    <svg class="card-icon" viewBox="0 0 48 48" aria-hidden="true">
      <rect x="4" y="4" width="40" height="40" rx="4" fill="none" stroke="var(--icon)" stroke-width="5"/>
      <path d="M24 12A12 12 0 1 0 36 24H24Z" fill="var(--blue)"/>
      <path d="M27 9A12 12 0 0 1 39 21H27Z" fill="var(--blue)"/>
    </svg>
    <p class="card-text">At the heart of our service is our proprietary redemption system used by the highest volume brands in the industry. Our redemption system generates real-time campaign analytics providing data to validate and enhance marketing decisions.</p>
  </article>

  <article class="card c2 r1">
    <h3 class="card-title">Security</h3>
    <svg class="card-icon" viewBox="0 0 48 48" aria-hidden="true">
      <path d="M14 22V15a10 10 0 0 1 20 0v7" fill="none" stroke="var(--icon)" stroke-width="5"/>
      <rect x="8" y="21" width="32" height="24" rx="3" fill="var(--icon)"/>
    </svg>
    <p class="card-text">We understand the impact that abuse from employees and customers have on the bottom line. We have a suite of security measures to stop abuse in its tracks. From single-use mobile coupons to detailed security reports you can rest assured that we have you covered.</p>
  </article>

  <article class="card c3 r1">
    <h3 class="card-title">Franchisee and Cooperative Friendly</h3>
    <svg class="card-icon" viewBox="0 0 48 48" aria-hidden="true">
      <path d="M24 20V28M10 34V28H38V34" fill="none" stroke="var(--blue)" stroke-width="2.5"/>
      <circle cx="24" cy="9" r="5" fill="var(--blue)"/><rect x="17" y="14" width="14" height="7" rx="3" fill="var(--blue)"/>
      <circle cx="10" cy="35" r="4.5" fill="var(--blue)"/><rect x="4" y="39" width="12" height="6" rx="3" fill="var(--blue)"/>
      <circle cx="38" cy="35" r="4.5" fill="var(--blue)"/><rect x="32" y="39" width="12" height="6" rx="3" fill="var(--blue)"/>
    </svg>
    <p class="card-text">Franchise owners can coordinate mobile marketing efforts with other franchise owners in their area. Our flexible setup allows for mobile coupons to be limited to a single franchisee or honored by adjoining franchisees or cooperative partners.</p>
  </article>

  <article class="card c1 r2">
    <h3 class="card-title">Target Customer Preferences</h3>
    <svg class="card-icon" viewBox="0 0 48 48" aria-hidden="true">
      <circle cx="24" cy="24" r="14" fill="none" stroke="var(--icon)" stroke-width="5"/>
      <path d="M24 2V16M24 32V46M2 24H16M32 24H46" stroke="var(--icon)" stroke-width="5"/>
    </svg>
    <p class="card-text">With a few clicks of a mouse, your mobile marketing campaign can be sent to all subscribers or a targeted group of subscribers. Send a breakfast offer to your breakfast customers, send a special offer to all non-redeemers, or send a mobile coupon to customers who like coffee. Targeted marketing has never been easier.</p>
  </article>

  <article class="card c2 r2">
    <h3 class="card-title">Social Media Integration</h3>
    <svg class="card-icon" viewBox="0 0 48 48" aria-hidden="true">
      <rect x="10" y="6" width="24" height="24" rx="3" fill="#3b5a96"/>
      <rect x="4" y="28" width="14" height="14" rx="3" fill="#c8282d"/>
      <rect x="24" y="28" width="16" height="14" rx="3" fill="#3fa9df"/>
    </svg>
    <p class="card-text">For many restaurateurs and retailers social media has become a way to engage with their customers. Our social campaigns can be shared on Friendsy, Chirpline, Pinboardly, or any other social media site. Our redemption system will track the impact of your social campaign and give you the same insight as with your mobile campaigns.</p>
  </article>

  <article class="card c3 r2">
    <h3 class="card-title">Agency Features</h3>
    <svg class="card-icon" viewBox="0 0 48 48" aria-hidden="true">
      <circle cx="24" cy="24" r="21" fill="var(--icon)"/>
      <path d="M27 8L15 27H23L20 40L33 20H25Z" fill="var(--white)"/>
    </svg>
    <p class="card-text">We provide all the tools necessary for a marketing agency to easily manage multiple clients. From differing access levels for your clients to A/B Testing, we have advanced agency features to manage the mobile marketing needs for your entire portfolio of clients.</p>
  </article>

  <article class="card c1 r3">
    <h3 class="card-title">Real-Time Analytics</h3>
    <svg class="card-icon" viewBox="0 0 48 48" aria-hidden="true">
      <rect x="4" y="8" width="40" height="28" rx="2" fill="none" stroke="var(--icon)" stroke-width="4"/>
      <rect x="1" y="37" width="46" height="5" rx="2" fill="var(--icon)"/>
      <path d="M10 29L18 20L25 25L37 14" fill="none" stroke="var(--blue)" stroke-width="3"/>
      <circle cx="18" cy="20" r="2.5" fill="var(--blue)"/><circle cx="25" cy="25" r="2.5" fill="var(--blue)"/>
    </svg>
    <p class="card-text">Unlike many other marketing options, mobile is easily measured. Our redemption system provides a rich set of analytics, including redemption reports, trend lines, even raw data if you like. Having historical and real-time data to slice, dice, and compare will make you a more effective marketer.</p>
  </article>

  <article class="card c2 r3">
    <h3 class="card-title">Direct Mail Integration</h3>
    <svg class="card-icon" viewBox="0 0 48 48" aria-hidden="true">
      <rect x="3" y="11" width="42" height="28" fill="none" stroke="var(--icon)" stroke-width="3.5"/>
      <path d="M4 12L24 28L44 12M4 38L18 24M44 38L30 24" fill="none" stroke="var(--icon)" stroke-width="3"/>
    </svg>
    <p class="card-text">Direct mail and paper coupons have long been staples in the marketing mix for restaurants and retail marketers. Our redemption system can be leveraged to provide in-depth analysis for those paper coupons, providing marketers the data to make more informed decisions. You can even kick start your mobile program through direct mail.</p>
  </article>

  <article class="card c3 r3">
    <h3 class="card-title">Proven Results</h3>
    <svg class="card-icon" viewBox="0 0 48 48" aria-hidden="true">
      <rect x="6" y="32" width="8" height="12" rx="2" fill="var(--icon)"/>
      <rect x="17" y="26" width="8" height="18" rx="2" fill="var(--icon)"/>
      <path d="M28 44V18H23L33 4L43 18H38V44Z" fill="var(--blue)"/>
    </svg>
    <p class="card-text">In today’s environment with DVRs, Reelnest, Smartphones, Orchard TV and a variety of other options, it’s becoming increasingly difficult to reach customers. Mobile marketing cuts through the clutter and puts your message directly in the pockets and purses of customers.</p>
  </article>

  <footer class="tagline">
    Qelvaro Powers Restaurants and Retail to Mobile Marketing Success<br>
    Increase Sales and Awareness with Marketing @ the Pace of TradeMind<sup>®</sup>
  </footer>
</section>

</body>
</html>
```